Business Card Design Project and Logo Enhancement

This project requires designing a business card for a construction company. It also requires small enhancements on provided logo.
Summary about the company:
Name: Korvellan Group.
Future website. www.korvellan.ca
Korvellan is a home redesign and renovation company providing services in Ottawa Canada area.
It offers the following services:
- Home Additions
- Roofing
- Eavestroughing & Soffit Fascia
- Fencing
- Decks
- Window Installation, and
- Indoor Renovation Including ( Kitchen redesign, Basement finishing, bathroom upgrades, etc)
Logo and Company name background:
Korvellan refers to an ancient empire that was located in Balkans called Veltarians.
Provided logo represents the symbol of Veltarians.
Project Expectation:
Logo:
Attached logo is too SIMPLe. It would be nice adding a bit of design.
That could include different colors or adding a bit of style to the logo.
Business Card
Initial preferred layout/content ( open to other suggestions) :
Preferred type: Vertical with rounded corners
Front side should have:
- Logo
- Company Name
- First Name/ Last name: Ie: Edmir Kollqaj
- Office Phone:
- Direct Phone:
- QR Code linking to www.korvellan.ca, and
- website url. www. korvellan.ca
Back end shall contain:
Professional services offered:
- Large company logo covering most of the card as a water mark
- Divisions Services offered
- Roofing
- Eavestroughing, Soffit, Fascia
- Fencing and Decks
- Indoor Design and Renovation
- Company Phone and
- Company website address: www.korvellan.ca
PSD and other raw files must be provided by the winner.

```html
<!DOCTYPE html>
<html lang="en">
<head>
<meta charset="utf-8">
<title>Korvellan Group – Business Card</title>
<link rel="stylesheet" href="https://fonts.googleapis.com/css2?family=Tinos:wght@400&display=swap">
<style>
  :root {
    --page-bg: #ffffff;
    --gold-edge: #b38f66;
    --gold-mid: #d9c3a0;
    --gold-light: #f6eedb;
    --brand-red: #6a1812;
    --name-red: #5a1510;
    --tagline-grey: #6c665d;
    --ink: #111111;
    --emblem-top: #e6e6e6;
    --emblem-bottom: #0e0e0e;
    --emblem-text: #ffffff;
  }
  html, body {
    margin: 0;
    padding: 0;
    width: 707px;
    height: 1200px;
    overflow: hidden;
    background: var(--page-bg);
  }
  .business-card {
    position: absolute;
    left: 8px;
    top: 8px;
    width: 681px;
    height: 1173px;
    border-radius: 32px;
    background: linear-gradient(90deg,
      var(--gold-edge) 0%,
      var(--gold-mid) 18%,
      var(--gold-light) 42%,
      var(--gold-mid) 72%,
      var(--gold-edge) 100%);
    box-shadow: 0 4px 6px rgba(0,0,0,0.45);
    font-family: "Tinos", "Times New Roman", serif;
    overflow: hidden;
  }
  .line {
    position: absolute;
    left: 0;
    width: 681px;
    margin: 0;
    padding-left: 16px;
    box-sizing: border-box;
    text-align: center;
    line-height: 1;
    white-space: nowrap;
    font-weight: 400;
  }
  .emblem {
    position: absolute;
    left: 228px;
    top: 74px;
    width: 240px;
    height: 240px;
  }
  .emblem-name {
    position: absolute;
    left: 228px;
    top: 180px;
    width: 240px;
    text-align: center;
    font-size: 30px;
    line-height: 1;
    color: var(--emblem-text);
  }
  .company-name { top: 367px; font-size: 63px; color: var(--brand-red); }
  .tagline { top: 430px; font-size: 34px; color: var(--tagline-grey); }
  .person-name { top: 594px; font-size: 63px; color: var(--name-red); }
  .contact { font-size: 33px; color: var(--ink); }
  .contact-office { top: 783px; }
  .contact-direct { top: 826px; }
  .contact-email { top: 872px; }
  .contact-web { top: 917px; }
  .service-area { top: 1074px; font-size: 23px; color: var(--ink); }
</style>
</head>
<body>
  <main class="business-card">
    <svg class="emblem" viewBox="0 0 240 240" aria-hidden="true">
      <defs>
        <linearGradient id="emblemFill" x1="0" y1="0" x2="0" y2="1">
          <stop offset="0" stop-color="#e6e6e6"/>
          <stop offset="1" stop-color="#0e0e0e"/>
        </linearGradient>
      </defs>
      <circle cx="120" cy="120" r="118" fill="url(#emblemFill)"/>
    </svg>
    <p class="emblem-name">Korvellan</p>

    <h1 class="line company-name">Korvellan Group</h1>
    <p class="line tagline">Home Redesign &amp; Renovation</p>

    <h2 class="line person-name">Edmir Kollqaj</h2>

    <p class="line contact contact-office">Office: 613.555.0142</p>
    <p class="line contact contact-direct">Direct: 613.555.0187</p>
    <p class="line contact contact-email">Email: contact@korvellan.ca</p>
    <p class="line contact contact-web">Web: www.korvellan.ca</p>

    <p class="line service-area">Providing Services in Ottawa Canada Area</p>
  </main>
</body>
</html>
```